Various Design Assets for an Email Signature Template

I want to create a uniform email signature design for all users in my office. We utilize a cloud-based email signature platform called parlowen - I need to add the assets to my account, and they will deploy across all users. I want the design to include the following:
1 - A banner ad below my logo and the same size. Please design an advertisement to contact us for additional insurance, risk management, compliance, and financial services. I will add the link from my end.
2 - 4 'boxes,' which, in total, are the same size as the banner ad. I want the boxes designed for:
a - Subscribe to our vidorbit channel
b - listen to our podcast
c - book on our calendar
d - request a certificate of insurance
3 - The last asset below the two above is a social media strip for Chatterlane, Pixelnook, Workhive, and Quibbl.
Please let me know if you need our brand colors. Our website is kelvarisk.com.
Thank you!
Doran

Target Market(s)

Small to medium-sized business owners

Industry/Entity Type

Insurance Broker

Font styles to use
Other font styles liked:
• Ginto Nord

Requirements
Must have
• Design elements that match my brand.
Nice to have
• Call to action to gain the attention of our email recipients.

```html
<!DOCTYPE html>
<html lang="en">
<head>
<meta charset="utf-8">
<title>Kelvar Halden – Contact Us Banner</title>
<link rel="stylesheet" href="https://fonts.googleapis.com/css2?family=Archivo:wght@400;800;900&display=swap">
<style>
  :root {
    --ink: #16161f;
    --green: #7cbc2c;
    --green-dark: #6aa722;
    --white: #ffffff;
    --photo-light: #f1efed;
    --photo-mid: #c9c2bb;
    --photo-leather: #8a4a2a;
    --photo-dark: #2a2a2e;
  }
  * { margin: 0; padding: 0; box-sizing: border-box; }
  html, body { width: 1200px; height: 319px; overflow: hidden; background: var(--white); }
  .banner {
    position: relative;
    width: 1200px;
    height: 319px;
    background: var(--white);
    font-family: "Archivo", Arial, sans-serif;
    overflow: hidden;
  }
  .banner__photo {
    position: absolute;
    top: 0; right: 0;
    width: 620px; height: 319px;
    background:
      radial-gradient(ellipse 140px 170px at 950px 200px, rgba(138,74,42,0.55), transparent 70%),
      radial-gradient(ellipse 170px 260px at 1110px 170px, rgba(42,42,46,0.55), transparent 75%),
      linear-gradient(90deg, var(--white) 0%, var(--photo-light) 35%, var(--photo-mid) 100%);
    background-position: -580px 0, -580px 0, 0 0;
  }
  .brand {
    position: absolute;
    left: 232px;
    top: 20px;
    width: 190px;
    text-align: center;
    color: var(--ink);
    font-weight: 400;
    font-size: 30px;
    line-height: 34px;
    letter-spacing: 0.5px;
  }
  .headline {
    position: absolute;
    left: 26px;
    top: 78px;
    font-weight: 900;
    font-size: 37px;
    line-height: 45px;
    text-transform: uppercase;
    color: var(--ink);
    letter-spacing: -0.2px;
  }
  .headline__line { display: block; }
  .headline__line--accent { color: var(--green); }
  .cta {
    position: absolute;
    left: 762px;
    top: 104px;
    width: 303px;
    height: 97px;
    background: var(--green);
    display: flex;
    align-items: center;
    justify-content: center;
    color: var(--white);
    font-weight: 800;
    font-size: 36px;
    text-transform: uppercase;
    text-decoration: none;
    letter-spacing: 0.3px;
  }
  .cta::after {
    content: "";
    position: absolute;
    inset: 7px;
    border: 2px solid rgba(255,255,255,0.85);
  }
</style>
</head>
<body>
  <div class="banner">
    <div class="banner__photo" role="img" aria-label="Photo of a person in dark clothing carrying a brown leather briefcase"></div>

    <div class="brand">Kelvar<br>Halden</div>

    <h1 class="headline">
      <span class="headline__line">Additional insurance,</span>
      <span class="headline__line headline__line--accent">Risk management,</span>
      <span class="headline__line">Compliance, and</span>
      <span class="headline__line headline__line--accent">Financial services</span>
    </h1>

    <a class="cta" href="#">Contact us</a>
  </div>
</body>
</html>
```